Modern and professional business card for medical weight management practice
Crestline Weight Management MD
Modern and professional business card for medical weight management practice - Health
Creative Brief
Professional
Tarlen Voskry M.D.
Medical Director
418 West Harlowe Court Suite B Sunnyvale, CA 94086
Will be provided
Crestlineweightcaremd@mailnest.example
Crestlineweightcaremd.example
Member of National Council of Metabolic Practice Member of United Academy of Clinical Associates Clinical Professor, PVMI Diplomate National council of Physicians
Have the appointment and the direction
Dravok Dravok
Please check private message.. Thanks.
brookvanehealth brookvanehealth
Hello Guys, Could you also include the following: Tarlen Voskry, M.D. Assistant Clinical Professor, PVMI Member of National Guild of Metabolic Clinicians
Hello guys, I have uploaded my new logo (Crestline Weight Management MD). Please forward me the designs. Thanks

```html
<!DOCTYPE html>
<html lang="en">
<head>
<meta charset="utf-8">
<title>Crestline Weight Management MD – Stationery Set</title>
<link rel="stylesheet" href="https://fonts.googleapis.com/css2?family=Open+Sans:wght@400;600;700&display=swap">
<style>
:root{
  --frame:#2a7fc0;
  --board:#a6a8ab;
  --blue:#1a7dc0;
  --navy:#1e3a6c;
  --grey:#6d6e71;
  --light-grey:#c9cacc;
  --paper:#ffffff;
  --ink:#4a4b4d;
  --faint:#e6edf4;
}
*{box-sizing:border-box;margin:0;padding:0}
html,body{width:1200px;height:974px;overflow:hidden}
body{font-family:"Open Sans",Arial,sans-serif;color:var(--ink);background:var(--frame)}
.board{position:absolute;left:16px;top:16px;width:1168px;height:942px;background:var(--board)}
.item{position:absolute;background:var(--paper);box-shadow:1px 2px 4px rgba(0,0,0,.25);overflow:hidden}
.wave{position:absolute;left:0;bottom:0;width:100%}
.brand{font-weight:700;color:var(--navy);text-transform:uppercase;letter-spacing:.04em;display:flex;align-items:center;gap:.35em;line-height:1}
.brand .dot{width:.7em;height:.7em;border-radius:50%;background:var(--blue);flex:none}
.brand .sub{display:block;font-size:.32em;letter-spacing:.12em;margin-top:.25em}
.tiny{font-size:4px;line-height:6px;color:var(--grey)}
.small{font-size:5px;line-height:7px;color:var(--grey)}
.faint-mark{position:absolute;border-radius:50%;background:var(--faint)}
/* main logo */
.main-brand{position:absolute;left:890px;top:50px;font-size:38px}
</style>
</head>
<body>
<div class="board">

  <!-- main logo -->
  <div class="main-brand brand" style="left:874px;top:52px"><span class="dot"></span><span>Crestline<span class="sub">Weight Management M.D.</span></span></div>

  <!-- business card back -->
  <div class="item card-back" style="left:55px;top:55px;width:179px;height:108px">
    <div class="tiny" style="position:absolute;left:8px;top:8px">Tarlen Voskry, M.D.<br>Medical Director</div>
    <div class="brand" style="position:absolute;left:80px;top:20px;font-size:12px"><span class="dot"></span>Crestline</div>
    <div class="tiny" style="position:absolute;left:80px;top:40px;width:92px">• Council of Metabolic Practice<br>• Academy of Clinical Associates<br>• Clinical Professor, PVMI</div>
    <svg class="wave" viewBox="0 0 100 20" preserveAspectRatio="none" height="22"><path d="M0 8 C30 18 60 0 100 10" stroke="var(--grey)" stroke-width="1" fill="none"/><path d="M0 12 C30 22 65 2 100 14 L100 20 L0 20Z" fill="var(--blue)"/></svg>
  </div>

  <!-- appointment card -->
  <div class="item appointment-card" style="left:55px;top:176px;width:179px;height:111px">
    <div class="small" style="position:absolute;left:10px;top:12px;font-weight:600;letter-spacing:.1em">APPOINTMENT</div>
    <div class="tiny" style="position:absolute;left:10px;top:34px;width:160px;display:grid;grid-template-columns:repeat(4,1fr);row-gap:6px">
      <span>□ Mon</span><span>□ Tue</span><span>□ Wed</span><span>□ Thu</span>
      <span>Date ______</span><span>Time ____</span><span>am/pm</span><span>□ Fri</span>
    </div>
    <svg class="wave" viewBox="0 0 100 20" preserveAspectRatio="none" height="22"><path d="M0 8 C30 18 60 0 100 10" stroke="var(--grey)" stroke-width="1" fill="none"/><path d="M0 12 C30 22 65 2 100 14 L100 20 L0 20Z" fill="var(--blue)"/></svg>
  </div>

  <!-- letterhead -->
  <div class="item letterhead" style="left:261px;top:55px;width:264px;height:356px">
    <div class="tiny" style="position:absolute;left:14px;top:12px">Crestline Weight Management MD<br>418 West Harlowe Court Suite B<br>Sunnyvale, CA 94086</div>
    <div class="brand" style="position:absolute;left:170px;top:22px;font-size:14px"><span class="dot"></span>Crestline</div>
    <div class="faint-mark" style="left:50px;top:70px;width:120px;height:120px"></div>
    <div class="tiny" style="position:absolute;left:0;right:0;bottom:8px;text-align:center">Crestlineweightcaremd.example</div>
    <svg class="wave" viewBox="0 0 100 20" preserveAspectRatio="none" height="30" style="bottom:16px"><path d="M0 6 C30 16 60 0 100 8" stroke="var(--grey)" stroke-width=".8" fill="none"/><path d="M0 10 C30 20 65 2 100 12" stroke="var(--blue)" stroke-width="3" fill="none"/></svg>
  </div>

  <!-- compliment slip -->
  <div class="item slip" style="left:569px;top:55px;width:114px;height:132px">
    <div class="brand" style="position:absolute;left:10px;top:12px;font-size:11px"><span class="dot"></span>Crestline</div>
    <div class="small" style="position:absolute;left:10px;top:42px;font-weight:600">With Compliments</div>
    <div class="tiny" style="position:absolute;left:10px;top:56px">Sunnyvale, CA 94086</div>
    <svg class="wave" viewBox="0 0 100 20" preserveAspectRatio="none" height="20"><path d="M0 8 C30 18 60 0 100 10" stroke="var(--grey)" stroke-width="1" fill="none"/><path d="M0 12 C30 22 65 2 100 14 L100 20 L0 20Z" fill="var(--blue)"/></svg>
  </div>

  <!-- business card front -->
  <div class="item card-front" style="left:569px;top:208px;width:167px;height:79px">
    <div class="tiny" style="position:absolute;left:8px;top:10px">Tarlen Voskry, M.D.<br>Medical Director<br>Tel (408) 555-0142</div>
    <div class="brand" style="position:absolute;left:92px;top:14px;font-size:11px"><span class="dot"></span>Crestline</div>
    <svg class="wave" viewBox="0 0 100 20" preserveAspectRatio="none" height="18"><path d="M0 8 C30 18 60 0 100 10" stroke="var(--grey)" stroke-width="1" fill="none"/><path d="M0 12 C30 22 65 2 100 14 L100 20 L0 20Z" fill="var(--blue)"/></svg>
  </div>

  <!-- DL envelope front -->
  <div class="item envelope-dl" style="left:569px;top:308px;width:240px;height:103px">
    <div class="tiny" style="position:absolute;left:10px;top:10px">418 West Harlowe Court Suite B<br>Sunnyvale, CA 94086</div>
    <div class="brand" style="position:absolute;left:150px;top:14px;font-size:13px"><span class="dot"></span>Crestline</div>
    <svg class="wave" viewBox="0 0 100 20" preserveAspectRatio="none" height="22"><path d="M0 8 C30 18 60 0 100 10" stroke="var(--grey)" stroke-width="1" fill="none"/><path d="M0 12 C30 22 65 2 100 14 L100 20 L0 20Z" fill="var(--blue)"/></svg>
  </div>

  <!-- envelope backs stack -->
  <svg class="envelope-stack" style="position:absolute;left:828px;top:282px" width="290" height="190" viewBox="0 0 290 190">
    <rect x="0" y="0" width="290" height="60" fill="var(--navy)"/>
    <path d="M0 0 L145 32 L290 0" fill="#2b4c85"/>
    <rect x="10" y="36" width="280" height="56" fill="var(--grey)"/>
    <path d="M10 36 L150 66 L290 36" fill="#808184"/>
    <rect x="20" y="70" width="270" height="56" fill="var(--blue)"/>
    <path d="M20 70 L155 100 L290 70" fill="#2b8fd0"/>
    <circle cx="155" cy="92" r="5" fill="#fff"/>
    <rect x="30" y="104" width="260" height="86" fill="#fff"/>
    <path d="M30 104 L160 138 L290 104" fill="none" stroke="var(--light-grey)"/>
    <text x="160" y="180" font-size="4" fill="var(--grey)" text-anchor="middle">Crestlineweightcaremd.example</text>
  </svg>

  <!-- presentation folder -->
  <div class="item folder" style="left:55px;top:480px;width:509px;height:401px">
    <div style="position:absolute;left:0;top:0;width:14px;height:100%;background:var(--blue)"></div>
    <div style="position:absolute;right:0;top:0;width:14px;height:100%;background:var(--blue)"></div>
    <div class="tiny" style="position:absolute;left:60px;top:20px">Crestline Weight Management MD<br>418 West Harlowe Court Suite B<br>Sunnyvale, CA 94086<br>Tel (408) 555-0142</div>
    <div class="faint-mark" style="left:30px;top:60px;width:140px;height:140px"></div>
    <div class="brand" style="position:absolute;left:120px;top:148px;font-size:30px"><span class="dot"></span><span>Crestline<span class="sub">Weight Management M.D.</span></span></div>
    <div class="tiny" style="position:absolute;left:60px;top:250px">Crestlineweightcaremd.example</div>
    <svg style="position:absolute;left:14px;bottom:0" width="481" height="130" viewBox="0 0 481 130" preserveAspectRatio="none">
      <path d="M0 30 C150 70 300 0 481 25" stroke="var(--blue)" stroke-width="5" fill="none"/>
      <path d="M0 40 C150 80 300 10 481 35 L481 130 L0 130Z" fill="var(--grey)"/>
      <path d="M190 60 L210 130 L290 130 L310 60" fill="#5d5e61"/>
    </svg>
    <div class="item" style="left:235px;top:324px;width:106px;height:53px">
      <div class="tiny" style="position:absolute;left:5px;top:6px">Tarlen Voskry, M.D.</div>
      <div class="brand" style="position:absolute;left:54px;top:20px;font-size:7px"><span class="dot"></span>Crestline</div>
    </div>
  </div>

  <!-- CD -->
  <svg class="cd" style="position:absolute;left:577px;top:498px" width="132" height="132" viewBox="0 0 132 132">
    <circle cx="66" cy="66" r="65" fill="#fff" stroke="var(--light-grey)"/>
    <path d="M2 80 C40 100 90 60 130 78" stroke="var(--blue)" stroke-width="5" fill="none"/>
    <circle cx="66" cy="66" r="12" fill="var(--board)" stroke="var(--light-grey)"/>
    <circle cx="30" cy="34" r="4" fill="var(--blue)"/>
    <text x="37" y="38" font-family="Open Sans, sans-serif" font-weight="700" font-size="12" fill="var(--navy)">CRESTLINE</text>
  </svg>

  <!-- CD sleeve -->
  <div class="item cd-sleeve" style="left:577px;top:630px;width:172px;height:224px">
    <div class="brand" style="position:absolute;left:22px;top:70px;font-size:16px"><span class="dot"></span><span>Crestline<span class="sub">Weight Management M.D.</span></span></div>
    <svg class="wave" viewBox="0 0 100 20" preserveAspectRatio="none" height="30" style="bottom:14px"><path d="M0 6 C30 16 60 0 100 8" stroke="var(--grey)" stroke-width=".8" fill="none"/><path d="M0 10 C30 20 65 2 100 12" stroke="var(--blue)" stroke-width="3" fill="none"/></svg>
  </div>

  <!-- fax sheet -->
  <div class="item fax" style="left:801px;top:485px;width:317px;height:390px">
    <div class="tiny" style="position:absolute;left:14px;top:12px">418 West Harlowe Court Suite B<br>Sunnyvale, CA 94086</div>
    <div class="brand" style="position:absolute;left:200px;top:18px;font-size:16px"><span class="dot"></span>Crestline</div>
    <div style="position:absolute;left:14px;top:56px;font-size:20px;font-weight:600;color:#222">Fax</div>
    <div class="tiny" style="position:absolute;left:14px;top:90px;width:290px;display:grid;grid-template-columns:1fr 1fr;row-gap:8px">
      <span>To: ____________________</span><span>From: __________________</span>
      <span>Fax: ___________________</span><span>Pages: _________________</span>
      <span>Phone: _________________</span><span>Date: __________________</span>
      <span>Re: ____________________</span><span>CC: ____________________</span>
    </div>
    <div style="position:absolute;left:14px;top:150px;width:290px;height:1px;background:var(--grey)"></div>
    <div class="tiny" style="position:absolute;left:14px;top:156px;width:290px;display:flex;justify-content:space-between">
      <span>■ Urgent</span><span>■ For Review</span><span>■ Please Comment</span><span>■ Please Reply</span>
    </div>
    <svg class="wave" viewBox="0 0 100 20" preserveAspectRatio="none" height="34" style="bottom:16px"><path d="M0 6 C30 16 60 0 100 8" stroke="var(--grey)" stroke-width=".8" fill="none"/><path d="M0 10 C30 20 65 2 100 12" stroke="var(--blue)" stroke-width="3" fill="none"/></svg>
  </div>

</div>
</body>
</html>
```